School Canteen Menu

We operate 30 school canteen/cafes across Melbourne. We are looking to update our old menu to a new attractive design.
We offer a variety of both food and drink and we need to highlight our healthy options. We would like to have a background picture of either salads or healthy sandwiche etc.
We have borken our current menu in catogories according to hot food, cold bar, drinks, ice creams etc.
We would prefer it to be a A4 design but other ideas are welcome.

In summary we need a vibrant attractive applealing design.
My business card with our lgo is also attached
Regards

Tam
Updates

We have two types of menu a secondary menu for students 12-18 and a primary school menu 5-12 year olds. I have attached samples of both.

Reason: Extended deadline as the director of business is away till sunday

Target Market(s)

12 year old to 18 year olds. School Students. As well as Teachers. Prehaps encouraging Teaches with our Freshly made salads will be a feature.

Industry/Entity Type

School

Requirements
Must have
• Viabrant Colors. Greens, Purples, Yellows.
Should not have
• Red Colors. Considered to be a unhealthy color.

```html
<!DOCTYPE html>
<html lang="en">
<head>
<meta charset="utf-8">
<title>Tamwood Kitchen – Canteen Menu 2012</title>
<link rel="stylesheet" href="https://fonts.googleapis.com/css2?family=Baloo+2:wght@700&family=Arimo:wght@400;700&display=swap">
<style>
  :root{
    --bg-dark:#8a3f16;
    --bg-mid:#c2652c;
    --bg-light:#d98a4c;
    --panel:rgba(255,240,240,.86);
    --purple:#8e1f7e;
    --green:#8cc63f;
    --white:#ffffff;
  }
  *{box-sizing:border-box;margin:0;padding:0}
  html,body{width:1200px;height:907px;overflow:hidden}
  body{position:relative;font-family:"Arimo",Arial,sans-serif;
    background:radial-gradient(ellipse at 30% 45%,var(--bg-light) 0%,var(--bg-mid) 45%,var(--bg-dark) 100%)}
  .backdrop-photo{position:absolute;left:0;top:0;width:1200px;height:907px;
    background:radial-gradient(ellipse 360px 420px at 330px 420px,rgba(120,70,40,.45),transparent 70%)}
  .menu-panel{position:absolute;left:32px;top:14px;width:556px;height:778px}
  .menu-panel > svg{position:absolute;inset:0}
  .badge{position:absolute;left:50%;transform:translateX(-50%);display:flex;align-items:center;justify-content:center;
    font-family:"Baloo 2",sans-serif;font-weight:700;color:var(--white);font-size:34px;line-height:1}
  .badge svg{position:absolute;inset:0;width:100%;height:100%}
  .badge span{position:relative;padding-top:4px}
  .item-list{position:absolute;left:38px;right:50px;list-style:none;color:var(--purple);font-size:13px;font-weight:700}
  .item{display:flex;align-items:flex-end;height:25.5px}
  .item .leader{flex:1;border-bottom:2px dotted var(--purple);margin:0 2px 4px;opacity:.8}
  .item-first-line{display:block;height:17px;line-height:17px;color:var(--purple);font-size:13px;font-weight:700}
  .item.after-first{height:19px}
  .mark{display:inline-block;width:18px;height:18px;border:1.5px solid #333;border-radius:50%;vertical-align:-4px;margin-left:1px}
  .legend{position:absolute;left:38px;top:682px;width:420px;color:var(--purple);font-size:13px;font-weight:700;line-height:21px}
  .legend .mark{width:34px;height:34px;border-width:2px;vertical-align:-8px;margin-right:4px}
  .photo{position:absolute}
  .photo-grid{position:absolute;left:613px;top:30px;width:557px;height:604px;border:2px solid var(--white);border-radius:8px;overflow:hidden;background:var(--white)}
  .brand-card{position:absolute;left:646px;top:228px;width:494px;height:155px;background:var(--white);
    display:flex;flex-direction:column;align-items:center;justify-content:center;gap:10px;color:var(--purple)}
  .brand-name{font-family:"Arimo",Arial,sans-serif;font-weight:700;font-size:38px;line-height:1}
  .brand-tag{font-family:"Arimo",Arial,sans-serif;font-weight:700;font-size:15px}
  .title{position:absolute;left:610px;width:560px;top:686px;text-align:center;font-family:"Baloo 2",sans-serif;font-weight:700;
    color:var(--white);font-size:46px;line-height:60px}
  .notice{position:absolute;left:620px;top:790px;width:550px;height:100px}
  .notice svg{position:absolute;inset:0;width:100%;height:100%}
  .notice p{position:relative;text-align:center;font-family:"Baloo 2",sans-serif;font-weight:700;color:var(--white);font-size:32px;line-height:38px;padding-top:12px}
</style>
</head>
<body>
  <div class="backdrop-photo" role="img" aria-label="Background photo of a burger on an orange table"></div>

  <section class="menu-panel">
    <svg width="556" height="778" viewBox="0 0 556 778" aria-hidden="true">
      <path fill="var(--panel)" d="M0 20 Q0 0 20 4 Q40 12 60 4 Q80 -2 100 6 Q120 12 140 4 Q160 -2 180 6 Q200 12 220 4 Q240 -2 260 6 Q280 12 300 4 Q320 -2 340 6 Q360 12 380 4 Q400 -2 420 6 Q440 12 460 4 Q480 -2 500 6 Q520 12 540 4 Q556 0 556 20 L556 778 L0 778 Z"/>
    </svg>

    <div class="badge" style="top:12px;width:160px;height:52px">
      <svg viewBox="0 0 160 52" preserveAspectRatio="none" aria-hidden="true"><path fill="var(--green)" d="M6 8 L150 3 L158 14 L152 26 L158 40 L148 50 L10 48 L2 38 L8 26 L1 14 Z"/></svg>
      <span>Snacks</span>
    </div>
    <ul class="item-list" style="top:64px">
      <li class="item"><span>Pikelets<i class="mark"></i></span><span class="leader"></span><span>$0.80</span></li>
      <li class="item"><span>Pop Corn<i class="mark"></i></span><span class="leader"></span><span>$2.00</span></li>
      <li class="item"><span>Fruit Salad – small<i class="mark"></i></span><span class="leader"></span><span>$1.50</span></li>
      <li class="item"><span>Fruit of the day<i class="mark"></i></span><span class="leader"></span><span>$0.80</span></li>
      <li class="item"><span>Jelly Cup with Fruit</span><span class="leader"></span><span>$1.50</span></li>
      <li class="item"><span>Anzac Cookie</span><span class="leader"></span><span>$2.00</span></li>
      <li class="item"><span>Mini Muffins (home baked)</span><span class="leader"></span><span>$0.80</span></li>
    </ul>

    <div class="badge" style="top:290px;width:150px;height:52px">
      <svg viewBox="0 0 150 52" preserveAspectRatio="none" aria-hidden="true"><path fill="var(--green)" d="M6 8 L140 3 L148 14 L142 26 L148 40 L138 50 L10 48 L2 38 L8 26 L1 14 Z"/></svg>
      <span>Drinks</span>
    </div>
    <ul class="item-list" style="top:353px">
      <li><span class="item-first-line">Flavoured Milk (3000ml) Chocolate,</span>
        <div class="item after-first"><span>Strawberry, Iced Coffee (FRESH)</span><span class="leader"></span><span>$2.50</span></div></li>
      <li class="item"><span>Water (600ml)<i class="mark"></i></span><span class="leader"></span><span>$2.30</span></li>
      <li class="item"><span>Fruit Juice (200ml) Tropical, Orange, Apple</span><span class="leader"></span><span>$1.50</span></li>
    </ul>

    <div class="badge" style="top:464px;width:200px;height:52px">
      <svg viewBox="0 0 200 52" preserveAspectRatio="none" aria-hidden="true"><path fill="var(--green)" d="M6 8 L190 3 L198 14 L192 26 L198 40 L188 50 L10 48 L2 38 L8 26 L1 14 Z"/></svg>
      <span>Ice Creams</span>
    </div>
    <ul class="item-list" style="top:524px">
      <li class="item"><span>Frozen Orange Wedge<i class="mark"></i></span><span class="leader"></span><span>$0.20</span></li>
      <li class="item"><span>Frozen Pineapple Ring<i class="mark"></i></span><span class="leader"></span><span>$0.50</span></li>
      <li class="item"><span>Frozen Fruit Yoghurt</span><span class="leader"></span><span>$2.00</span></li>
      <li class="item"><span>Zippy Freezer</span><span class="leader"></span><span>$0.80</span></li>
      <li class="item"><span>Sunny Pop_Orange, Lemonade</span><span class="leader"></span><span>$2.00</span></li>
    </ul>

    <p class="legend"><i class="mark"></i>Foods marked with a circle are green foods and can be<br>eaten everyday</p>
  </section>

  <div class="photo" style="left:3px;top:792px;width:190px;height:115px;background:linear-gradient(135deg,#f4e45a,#6cc3d9 60%,#e23a4a)" role="img" aria-label="Photo of a strawberry smoothie"></div>
  <div class="photo" style="left:197px;top:792px;width:193px;height:115px;background:linear-gradient(135deg,#c9d3e4,#f2ecdc 60%,#e6c98a)" role="img" aria-label="Photo of a bowl of popcorn"></div>
  <div class="photo" style="left:396px;top:792px;width:192px;height:115px;background:linear-gradient(135deg,#f0f0f0,#e6e6e6 50%,#d8345c)" role="img" aria-label="Photo of berry sorbet with strawberries"></div>

  <div class="photo-grid">
    <div class="photo" style="left:0;top:0;width:276px;height:258px;background:linear-gradient(135deg,#e5d54c,#d83b2a 50%,#4f8e3a)" role="img" aria-label="Photo of a fresh garden salad"></div>
    <div class="photo" style="left:280px;top:0;width:277px;height:258px;background:linear-gradient(135deg,#f1eee0,#a9c86a 60%,#4c8a2e)" role="img" aria-label="Photo of a salad wrap"></div>
    <div class="photo" style="left:0;top:262px;width:276px;height:342px;background:radial-gradient(circle at 50% 55%,#c9813c,#a35d26 60%,#e9e2d8)" role="img" aria-label="Photo of oat cookies on a plate"></div>
    <div class="photo" style="left:280px;top:262px;width:277px;height:342px;background:radial-gradient(circle at 55% 60%,#e8d7b0,#cfae72 55%,#f3f0ea)" role="img" aria-label="Photo of crumbed chicken bites with sauce"></div>
  </div>

  <div class="brand-card">
    <div class="brand-name">Tamwood Kitchen</div>
    <div class="brand-tag">Healthy and Nutritious School Catering</div>
  </div>

  <h1 class="title">Canteen Menu 2012</h1>

  <div class="notice">
    <svg viewBox="0 0 550 100" preserveAspectRatio="none" aria-hidden="true"><path fill="var(--green)" d="M8 8 L540 2 L548 20 L542 50 L550 80 L536 98 L14 96 L0 78 L6 50 L2 20 Z"/></svg>
    <p>Canteen Closed<br>on Tuesdays &amp; Wednesday’s</p>
  </div>
</body>
</html>
```